Nutritional neuroscience book cover design*

We need a book cover design for a new book on nutritional neuroscience and aging. The book is written for the general public and answers questions such as, "We are living longer than ever. The problem is, will our brain stay healthy as we age? We certainly do not want to live longer with various diseases, in particular brain diseases. How does the brain change during aging? And what can we do to promote the health of our brain and prevent and treat neurological diseases that typically occur during the aging process?" Based on recent discoveries in the field of nutritional neuroscience, this book presents how we can use nutrition to help our brain stay healthy longer. While our brain shrinks and becomes functionally weaker during the aging process, nutrition is able to slow this process down. This book illustrates this point through chapters on stroke, Parkinson’s disease, Multiple Sclerosis, dementia, depression, anxiety, and schizophrenia. The book will appeal to anyone looking to optimize their brain’s health and performance today and decades into the future.

Target Market(s)

General audience

Colors

Designer to choose colors to be used in the design.

Requirements
Must have
• Title: Meals Across the Decades: A Field Guide to Diet and the Mind
• Edited by Corinne T. Halvorsen, Ph.D.
• Book size: 7*10 inches
• Backcover text:
• Humans are living longer than ever. How does the brain change during aging? Will our brain stay healthy as we age? We certainly do not want to live longer with neurological diseases. What can we do to promote the health of our brain?
• Based on recent discoveries in the field of nutritional neuroscience, this book presents how nutrition affects our brain health. While we age, our brain shrinks and there are changes in how it functions, nutrition is an important component that can help maintain optimal brain health.
• Using scientific evidence, this book illustrates the importance of nutrition for neurological diseases including Alzheimer’s disease, stroke, Parkinson’s disease, Multiple Sclerosis, vascular dementia, depression, anxiety, and schizophrenia. This book will appeal to anyone looking to learn more about how nutrition affects brain health.

```html
<!DOCTYPE html>
<html lang="en">
<head>
<meta charset="utf-8">
<title>Meals Across the Decades: A Field Guide to Diet and the Mind</title>
<link rel="stylesheet" href="https://fonts.googleapis.com/css2?family=Fredoka:wght@600&family=EB+Garamond:wght@400;500&display=swap">
<style>
  :root {
    --page-bg: #f2f2f2;
    --sky-top: #b3e8fa;
    --sky-mid: #a8def4;
    --sky-low: #bfe6f3;
    --grass-light: #7cc24a;
    --grass-dark: #3f8f2a;
    --title-blue: #0b5b8e;
    --title-deep: #074a77;
    --ink: #141414;
    --paper-white: #ffffff;
  }
  * { margin: 0; padding: 0; box-sizing: border-box; }
  html, body {
    width: 1200px;
    height: 800px;
    overflow: hidden;
    background: var(--page-bg);
  }
  .canvas {
    position: relative;
    width: 1200px;
    height: 800px;
  }
  .cover {
    position: absolute;
    left: 348px;
    top: 40px;
    width: 504px;
    height: 720px;
    overflow: hidden;
    box-shadow: 0 10px 30px rgba(0,0,0,0.12);
  }
  .cover-photo {
    position: absolute;
    inset: 0;
    background: linear-gradient(180deg,
      var(--sky-top) 0%,
      var(--sky-mid) 55%,
      var(--sky-low) 83%,
      var(--grass-light) 87%,
      var(--grass-dark) 100%);
  }
  .title {
    position: absolute;
    top: 68px;
    left: 0;
    right: 0;
    text-align: center;
    font-family: "Fredoka", sans-serif;
    font-weight: 600;
    color: var(--title-blue);
    text-transform: uppercase;
    line-height: 1;
  }
  .title-top {
    display: block;
    font-size: 74px;
    letter-spacing: 1px;
    color: var(--title-deep);
  }
  .title-link {
    display: flex;
    align-items: center;
    justify-content: center;
    gap: 14px;
    margin-top: 8px;
    font-size: 34px;
    color: var(--title-deep);
  }
  .title-rule {
    width: 70px;
    height: 3px;
    background: var(--title-deep);
    border-radius: 2px;
  }
  .title-main {
    display: block;
    margin-top: 8px;
    font-size: 92px;
    letter-spacing: 1px;
  }
  .subtitle {
    position: absolute;
    top: 372px;
    left: 0;
    right: 0;
    text-align: center;
    font-family: "EB Garamond", serif;
    font-weight: 400;
    font-size: 24px;
    line-height: 1.45;
    letter-spacing: 5px;
    color: var(--ink);
    text-transform: uppercase;
  }
  .editor {
    position: absolute;
    bottom: 28px;
    left: 0;
    right: 0;
    text-align: center;
    font-family: "EB Garamond", serif;
    font-weight: 500;
    font-size: 24px;
    letter-spacing: 1px;
    color: var(--paper-white);
  }
  .editor-name {
    text-transform: uppercase;
    letter-spacing: 2px;
  }
</style>
</head>
<body>
  <main class="canvas">
    <section class="cover">
      <div class="cover-photo" role="img" aria-label="Photograph of an older couple riding a bicycle along a grassy dike under a bright blue summer sky with light clouds"></div>
      <h1 class="title">
        <span class="title-top">Meals</span>
        <span class="title-link"><span class="title-rule"></span>Across the<span class="title-rule"></span></span>
        <span class="title-main">Decades</span>
      </h1>
      <p class="subtitle">A Field Guide<br>to Diet and<br>the Mind</p>
      <p class="editor">Edited by <span class="editor-name">Corinne T. Halvorsen</span></p>
    </section>
  </main>
</body>
</html>
```